I need a folder to put papers in when I am scheduling patients for surgery. The information is general, such as costs, consent forms etc. The folder is designed to give the patient these papers in a neat manner. The cover of the folder needs to use my brand and perhaps create some interest when it is sitting on their kitchen bench with visitors and family. I'll attach a typical template for a folder. It needs to be stylish, classic and professional, as I am about to operate on the person's eye. <br/>I would like my logo included. I'll also attach a photo which is on my website which might work to wrap around the folder. The website address is bramwelkoske.com.au and you can see the way the image is used there on most of the pages as a banner. My profile photo could possibly used as well. Perhaps on the back, but if it looks strange then that is not necessary. The contact information need not be on the folder. Just Dr Lars Brimwell, Ophthalmic Surgeon. Finally, our brand slogan is. "The world's a beautiful place, see it clearly". This could also be on it. Again, this all needs to be professional looking. <br/>I've attached all our previous design jobs, 2 profile pictures, and the image that I think would work. Please also look at the website. <br/><br/>The second part of the project is to create a business card for my practice manager. Her name is Fiona Pelkrest<br/>It should include<br/>Fiona Pelkrest (BCom)<br/>Practice Manager for Dr Lars Brimwell<br/>Ophthalmic Surgeon <br/><br/>Then all the details which are on our current business card<br/><br/><br/><br/><br/>

Contact Information for Business Card

Just match the business cards I already have, but use the details above

Colors

Designer to choose colors to be used in the design.

```html
<!DOCTYPE html>
<html lang="en">
<head>
<meta charset="utf-8">
<title>Dr Lars Brimwell – Patient Folder</title>
<link rel="stylesheet" href="https://fonts.googleapis.com/css2?family=Open+Sans:wght@400;600;700&family=Quicksand:wght@300&display=swap">
<style>
  :root{
    --page:#e9eaeb;
    --paper:#f4f5f6;
    --paper-shade:#e6e8ea;
    --brand:#2f7fc1;
    --brand-light:#4a9ad6;
    --ink:#3d4550;
    --muted:#6b7480;
    --sun-top:#3b3a38;
    --sun-mid:#c98a2e;
    --sun-glow:#f2c14e;
    --sea:#5a5242;
    --portrait-bg:#b9b2a6;
    --portrait-suit:#3a3f47;
  }
  *{margin:0;padding:0;box-sizing:border-box}
  html,body{width:802px;height:1200px;overflow:hidden;background:var(--page)}
  .canvas{position:relative;width:802px;height:1200px}
  .folder{
    position:absolute;left:201px;width:400px;height:565px;
    background:linear-gradient(160deg,var(--paper) 0%,var(--paper) 55%,var(--paper-shade) 100%);
    box-shadow:0 2px 6px rgba(0,0,0,.12);overflow:hidden;
  }
  .folder--front{top:15px}
  .folder--back{top:612px}

  /* front */
  .brand{position:absolute;left:16px;top:26px;display:flex;align-items:center;gap:8px;width:150px}
  .brand__dot{width:22px;height:22px;border-radius:50%;background:var(--brand);flex:none}
  .brand__name{font:600 13px/1.1 "Open Sans",sans-serif;color:var(--brand)}
  .brand__role{font:600 7px/1.3 "Open Sans",sans-serif;color:var(--ink);margin-top:2px}
  .brand__creds{font:400 5px/1.3 "Open Sans",sans-serif;color:var(--muted)}
  .banner{
    position:absolute;left:150px;top:0;width:250px;height:118px;
    background:linear-gradient(180deg,var(--sun-top) 0%,var(--sun-mid) 45%,var(--sun-glow) 55%,var(--sea) 70%,var(--sun-top) 100%);
  }
  .rule{position:absolute;left:0;width:100%;background:var(--brand)}
  .rule--banner{top:118px;height:4px}
  .rule--mid{top:322px;height:5px;background:linear-gradient(90deg,var(--brand),var(--brand-light))}
  .rule--foot{top:520px;height:4px}
  .slogan{position:absolute;right:26px;top:140px;text-align:right;font-family:"Quicksand",sans-serif;font-weight:300;color:var(--brand)}
  .slogan__lead{font-size:31px;line-height:1.05}
  .slogan__call{font-size:50px;line-height:.95;margin-top:6px}
  .site{position:absolute;right:26px;top:372px;font:700 12px "Open Sans",sans-serif;color:var(--brand)}

  /* back */
  .rule--back{top:430px;height:4px}
  .rule--back-foot{top:520px;height:4px;width:40px}
  .portrait{position:absolute;left:40px;top:442px;width:140px;height:100px;
    background:linear-gradient(180deg,var(--portrait-bg) 0%,var(--portrait-bg) 55%,var(--portrait-suit) 100%)}
  .contact{position:absolute;left:192px;top:446px;list-style:none;font:400 8px/1.45 "Open Sans",sans-serif;color:var(--ink)}
  .contact li{display:flex;align-items:center;gap:5px}
  .contact svg{width:8px;height:8px;flex:none}
  .contact .address{margin-top:5px;padding-left:13px}
</style>
</head>
<body>
<main class="canvas">

  <section class="folder folder--front" aria-label="Folder front cover">
    <div class="brand">
      <span class="brand__dot"></span>
      <div>
        <div class="brand__name">Dr Lars Brimwell</div>
        <div class="brand__role">Ophthalmic Surgeon</div>
        <div class="brand__creds">Eye Surgery Specialist</div>
      </div>
    </div>
    <div class="banner" role="img" aria-label="Photograph of a sunset over the ocean"></div>
    <div class="rule rule--banner"></div>
    <h1 class="slogan">
      <span class="slogan__lead">The world's<br>a beautiful place</span><br>
      <span class="slogan__call">See it<br>clearly</span>
    </h1>
    <div class="rule rule--mid"></div>
    <p class="site">bramwelkoske.com.au</p>
    <div class="rule rule--foot"></div>
  </section>

  <section class="folder folder--back" aria-label="Folder back cover">
    <div class="rule rule--back"></div>
    <div class="rule rule--back-foot"></div>
    <div class="portrait" role="img" aria-label="Portrait photograph of Dr Lars Brimwell"></div>
    <ul class="contact">
      <li><svg viewBox="0 0 10 10"><circle cx="5" cy="5" r="5" fill="var(--brand)"/></svg>(08) 9420 3117</li>
      <li><svg viewBox="0 0 10 10"><circle cx="5" cy="5" r="5" fill="var(--brand)"/></svg>(08) 9420 3118</li>
      <li><svg viewBox="0 0 10 10"><circle cx="5" cy="5" r="5" fill="var(--brand)"/></svg>reception@bramwelkoske.com.au</li>
      <li class="address">24 Harlow Street, Kelmscott<br>Western Australia 6111</li>
    </ul>
  </section>

</main>
</body>
</html>
```